Beauty website banner

We are an Australian beauty website selling mid and high end cosmetics and beauty products.

We need a banner that tells customers they can share their product wishlists with friends to let them know what they want for Christmas.

Target Market(s)

Female, 30-60, white collar

Industry/Entity Type

Cosmetics

Requirements
Must have
• 600 x 150 pixels in size

Words to be as follows, not including the (") of course.

"Share your wishlist with friends and family for Christmas!"

(Then in smaller font) "Just log in to your account, go to your wishlist and click on the ‘share wishlist’ button"

```html
<!DOCTYPE html>
<html lang="en">
<head>
<meta charset="utf-8">
<title>Share your wishlist – Christmas banner</title>
<link rel="stylesheet" href="https://fonts.googleapis.com/css2?family=Nunito:wght@400;600&display=swap">
<style>
  :root {
    --sky-top: #e4f1fb;
    --sky-bottom: #bcdcf3;
    --headline-blue: #1b6cab;
    --band-blue: #0e5c9a;
    --band-text: #ffffff;
    --button-pink: #e6216e;
    --heart-pink: #ec2a74;
    --frost: #7fb6e0;
    --bottle-light: #e8c4ec;
    --bottle-deep: #a163b8;
  }
  * { margin: 0; padding: 0; box-sizing: border-box; }
  html, body { width: 1200px; height: 300px; overflow: hidden; }
  body { font-family: "Nunito", sans-serif; }

  .banner {
    position: relative;
    width: 1200px;
    height: 300px;
    overflow: hidden;
    background: radial-gradient(ellipse at 70% 30%, var(--sky-top) 0%, var(--sky-bottom) 100%);
  }

  .product-shot {
    position: absolute;
    left: 8px;
    top: 0;
    width: 184px;
    height: 232px;
    border-radius: 40px 40px 60px 60px;
    background: radial-gradient(ellipse at 50% 70%, var(--bottle-light) 0%, var(--bottle-deep) 100%);
    opacity: 0.85;
  }

  .frost-accent {
    position: absolute;
    left: 985px;
    top: 74px;
    width: 112px;
    height: 78px;
    border-radius: 40px;
    background: radial-gradient(circle, var(--frost) 0%, rgba(127,182,224,0) 70%);
  }

  .headline {
    position: absolute;
    left: 204px;
    top: 34px;
    color: var(--headline-blue);
    font-weight: 400;
    letter-spacing: -0.5px;
  }
  .headline__main {
    display: block;
    font-size: 72px;
    line-height: 92px;
  }
  .headline__sub {
    display: block;
    font-size: 50px;
    line-height: 64px;
  }
  .heart-i { position: relative; }
  .heart-i__mark {
    position: absolute;
    left: 50%;
    top: 4px;
    width: 22px;
    height: 20px;
    transform: translateX(-50%);
  }

  .instruction-band {
    position: absolute;
    left: 0;
    bottom: 0;
    width: 1200px;
    height: 62px;
    background: var(--band-blue);
    display: flex;
    align-items: center;
    padding-left: 86px;
    color: var(--band-text);
    font-size: 26px;
    font-weight: 400;
    white-space: nowrap;
  }
  .share-button {
    display: inline-block;
    margin: 0 14px;
    padding: 0 20px;
    height: 40px;
    line-height: 40px;
    border-radius: 8px;
    background: var(--button-pink);
    color: var(--band-text);
    font-size: 25px;
  }
</style>
</head>
<body>
  <div class="banner">
    <div class="product-shot" role="img" aria-label="Rosa Bloom perfume bottle with a red flower cap"></div>
    <div class="frost-accent" role="img" aria-label="Snowflake decoration"></div>

    <h1 class="headline">
      <span class="headline__main">Share your wishl<span class="heart-i">ı<svg class="heart-i__mark" viewBox="0 0 22 20" aria-hidden="true"><path fill="var(--heart-pink)" d="M11 19 C4 13 0 10 0 5.5 C0 2.5 2.4 0 5.5 0 C8 0 9.8 1.5 11 3.5 C12.2 1.5 14 0 16.5 0 C19.6 0 22 2.5 22 5.5 C22 10 18 13 11 19 Z"/></svg></span>st</span>
      <span class="headline__sub">with friends and family for Christmas!</span>
    </h1>

    <div class="instruction-band">
      Just log in to your account, go to your wishlist and click on the
      <span class="share-button">Share Wishlist</span>
      button
    </div>
  </div>
</body>
</html>
```